R&t Subterra

We specialize in CIPP pipe lining but do other underground utilities trenchless as well.

Target Market(s)

Trenchless sewer replacement

Contact Information for Business Card

Gavin Holtby 715-482-6130 Tamarack Hollow, wi

```html
<!DOCTYPE html>
<html lang="en">
<head>
<meta charset="utf-8">
<title>R&amp;T Subterra – Business Card</title>
<link rel="stylesheet" href="https://fonts.googleapis.com/css2?family=Montserrat:wght@400;600;700&display=swap">
<style>
  :root {
    --backdrop: #707070;
    --card-white: #ffffff;
    --sky-blue: #53b1e4;
    --deep-blue: #3490cc;
    --stone-grey: #ababab;
    --text-grey: #9b9b9b;
    --rule-grey: #cfcfcf;
  }
  html, body {
    margin: 0;
    padding: 0;
    width: 1200px;
    height: 1000px;
    overflow: hidden;
    background: var(--backdrop);
    font-family: "Montserrat", sans-serif;
  }
  .canvas {
    position: relative;
    width: 1200px;
    height: 1000px;
  }
  .card {
    position: absolute;
    left: 325px;
    width: 612px;
    height: 351px;
    border-radius: 20px;
    overflow: hidden;
  }
  .card-front {
    top: 95px;
    background: var(--sky-blue);
  }
  .card-back {
    top: 504px;
    background: var(--card-white);
  }
  .front-wordmark {
    position: absolute;
    right: 48px;
    top: 274px;
    margin: 0;
    color: var(--card-white);
    font-weight: 700;
    font-size: 26px;
    line-height: 32px;
    letter-spacing: 0.5px;
  }
  .back-brand {
    position: absolute;
    left: 30px;
    top: 36px;
    display: flex;
    align-items: center;
    gap: 12px;
  }
  .brand-dot {
    width: 44px;
    height: 44px;
    border-radius: 50%;
    background: var(--deep-blue);
  }
  .back-wordmark {
    margin: 0;
    color: var(--deep-blue);
    font-weight: 700;
    font-size: 24px;
    letter-spacing: 0.5px;
  }
  .divider {
    position: absolute;
    left: 33px;
    top: 121px;
    width: 545px;
    height: 1px;
    background: var(--rule-grey);
  }
  .holder-name {
    position: absolute;
    left: 76px;
    top: 204px;
    margin: 0;
    font-weight: 700;
    font-size: 21px;
    line-height: 28px;
    letter-spacing: 0.3px;
  }
  .holder-name .first { color: var(--deep-blue); }
  .holder-name .last { color: var(--sky-blue); }
  .contact-list {
    position: absolute;
    left: 347px;
    top: 192px;
    margin: 0;
    padding: 0;
    list-style: none;
    color: var(--text-grey);
    font-size: 17.5px;
    line-height: 24px;
  }
  .contact-list li {
    display: flex;
    align-items: center;
    gap: 8px;
  }
  .contact-list svg { flex: none; }
  .colour-bands {
    position: absolute;
    left: 0;
    bottom: 0;
    width: 100%;
    height: 24px;
    display: flex;
  }
  .band-grey { width: 145px; background: var(--stone-grey); }
  .band-deep { width: 191px; background: var(--deep-blue); }
  .band-sky { flex: 1; background: var(--sky-blue); }
</style>
</head>
<body>
<main class="canvas">
  <section class="card card-front" aria-label="Card front">
    <p class="front-wordmark">R&amp;T SUBTERRA</p>
  </section>

  <section class="card card-back" aria-label="Card back">
    <div class="back-brand">
      <span class="brand-dot"></span>
      <p class="back-wordmark">R&amp;T SUBTERRA</p>
    </div>
    <div class="divider"></div>
    <h1 class="holder-name"><span class="first">GAVIN</span> <span class="last">HOLTBY</span></h1>
    <ul class="contact-list">
      <li>
        <svg width="11" height="16" viewBox="0 0 11 16" aria-hidden="true">
          <rect x="1" y="1" width="9" height="14" rx="1.5" fill="none" stroke="#53b1e4" stroke-width="1.6"/>
          <rect x="4" y="12" width="3" height="1.4" fill="#53b1e4"/>
        </svg>
        715-482-6130
      </li>
      <li>
        <svg width="11" height="14" viewBox="0 0 11 14" aria-hidden="true">
          <path d="M5.5 0.5C2.8 0.5 0.8 2.5 0.8 5.1 0.8 8.4 5.5 13.5 5.5 13.5S10.2 8.4 10.2 5.1C10.2 2.5 8.2 0.5 5.5 0.5Z" fill="#53b1e4"/>
          <circle cx="5.5" cy="5.1" r="1.7" fill="#ffffff"/>
        </svg>
        Tamarack Hollow
      </li>
    </ul>
    <div class="colour-bands">
      <span class="band-grey"></span>
      <span class="band-deep"></span>
      <span class="band-sky"></span>
    </div>
  </section>
</main>
</body>
</html>
```